Committee to Elect Tall Ned Marsh County Commissioner District 1

I need a patriotic Background with Bold Red White and Blue Colors with a steel'ish look. The Front will say "Vote Tall Ned Marsh County Commissioner" With an Emphasis on the name "Marsh" The back needs to be simple color that allows for readable lines. It will have my website, phone, email and facebook links on the back and in small but readable print on the bottom it will say "Paid for by the Committe to Elect Tall Ned Marsh County Commissiner"

```html
<!DOCTYPE html>
<html lang="en">
<head>
<meta charset="utf-8">
<title>Tall Ned Marsh – County Commissioner Card</title>
<link rel="stylesheet" href="https://fonts.googleapis.com/css2?family=Poppins:wght@400;500;600;800&display=swap">
<style>
  :root {
    --page: #f1f1f1;
    --navy-deep: #0c1f3c;
    --navy-glow: #16406e;
    --red: #ed1c24;
    --red-dark: #c01c2e;
    --white: #ffffff;
    --ink-shadow: #1a1440;
  }
  * { margin: 0; padding: 0; box-sizing: border-box; }
  html, body { width: 1200px; height: 1200px; overflow: hidden; }
  body {
    background: var(--page);
    font-family: "Poppins", sans-serif;
    color: var(--white);
    position: relative;
  }
  .card {
    position: absolute;
    left: 232px;
    width: 736px;
    height: 441px;
    overflow: hidden;
    box-shadow: 0 4px 14px rgba(0, 0, 0, 0.35);
  }
  .card--front { top: 106px; }
  .card--back { top: 602px; }
  .card__art { position: absolute; inset: 0; width: 100%; height: 100%; }
  .card__text { position: absolute; white-space: nowrap; line-height: 1; }

  .headline-vote {
    left: 72px; top: 93px;
    font-size: 58px; font-weight: 600;
    text-shadow: 3px 3px 0 var(--ink-shadow);
  }
  .headline-name {
    left: 68px; top: 135px;
    font-size: 130px; font-weight: 800; letter-spacing: -3px;
    text-shadow: 4px 4px 0 var(--ink-shadow);
  }
  .headline-office {
    left: 72px; top: 250px;
    font-size: 30px; font-weight: 600;
    text-shadow: 2px 2px 0 var(--ink-shadow);
  }

  .contact-list { position: absolute; left: 376px; top: 131px; list-style: none; }
  .contact-item {
    display: flex; align-items: center; gap: 9px;
    height: 35px;
    font-size: 22px; font-weight: 400;
  }
  .contact-icon { width: 26px; height: 26px; flex: none; }

  .disclaimer {
    position: absolute; left: 67px; top: 282px;
    font-size: 19.5px; font-weight: 400; line-height: 25px;
  }
</style>
</head>
<body>
  <svg width="0" height="0" style="position:absolute">
    <defs>
      <radialGradient id="navy-field" cx="0.55" cy="0.5" r="0.7">
        <stop offset="0" stop-color="#16406e"/>
        <stop offset="1" stop-color="#0c1f3c"/>
      </radialGradient>
      <linearGradient id="red-field" x1="0" y1="0" x2="1" y2="0">
        <stop offset="0" stop-color="#c01c2e"/>
        <stop offset="0.45" stop-color="#ed1c24"/>
        <stop offset="0.8" stop-color="#ed1c24"/>
        <stop offset="1" stop-color="#c01c2e"/>
      </linearGradient>
    </defs>
  </svg>

  <section class="card card--front">
    <svg class="card__art" viewBox="0 0 1184 710" preserveAspectRatio="none" role="img" aria-label="Navy field with faint star pattern above red and white waves">
      <rect width="1184" height="710" fill="url(#navy-field)"/>
      <path d="M0,480 C150,580 300,630 450,610 C650,585 800,450 950,370 C1050,320 1120,300 1184,298 L1184,710 L0,710 Z" fill="#ffffff"/>
      <path d="M0,582 C120,630 250,660 400,645 C600,620 750,500 900,430 C1000,385 1100,370 1184,385 L1184,710 L0,710 Z" fill="url(#red-field)"/>
    </svg>
    <div class="card__text headline-vote">Vote Tall Ned</div>
    <div class="card__text headline-name">Marsh</div>
    <div class="card__text headline-office">County Commissioner</div>
  </section>

  <section class="card card--back">
    <svg class="card__art" viewBox="0 0 1184 710" preserveAspectRatio="none" role="img" aria-label="Navy field with faint star pattern above red and white waves">
      <rect width="1184" height="710" fill="url(#navy-field)"/>
      <path d="M0,300 C150,285 300,320 450,400 C600,480 700,590 850,612 C1000,630 1100,560 1184,480 L1184,710 L0,710 Z" fill="#ffffff"/>
      <path d="M0,378 C150,365 300,380 450,440 C600,500 700,620 850,645 C1000,665 1100,620 1184,582 L1184,710 L0,710 Z" fill="url(#red-field)"/>
    </svg>

    <ul class="contact-list">
      <li class="contact-item">
        <svg class="contact-icon" viewBox="0 0 26 26" fill="none" stroke="#fff" stroke-width="1.4">
          <circle cx="13" cy="13" r="12"/>
          <path d="M8.5 7.5 l2.5 -0.5 l1.3 3 l-1.5 1.2 c0.8 1.8 2 3 3.8 3.8 l1.2 -1.5 l3 1.3 l-0.5 2.5 c-5 0.5 -10.3 -4.8 -9.8 -9.8 z" fill="#fff" stroke="none"/>
        </svg>
        <span>123 456 7890</span>
      </li>
      <li class="contact-item">
        <svg class="contact-icon" viewBox="0 0 26 26" fill="none" stroke="#fff" stroke-width="1.4">
          <circle cx="13" cy="13" r="12"/>
          <rect x="7" y="9" width="12" height="8.5"/>
          <path d="M7 9 l6 5 l6 -5 M7 17.5 l4.5 -4 M19 17.5 l-4.5 -4"/>
        </svg>
        <span>yourname@mailbox.com</span>
      </li>
      <li class="contact-item">
        <svg class="contact-icon" viewBox="0 0 26 26" fill="none" stroke="#fff" stroke-width="1.4">
          <circle cx="13" cy="13" r="12"/>
          <circle cx="13" cy="13" r="6.5"/>
          <ellipse cx="13" cy="13" rx="3" ry="6.5"/>
          <path d="M6.5 13 h13 M7.5 10 h11 M7.5 16 h11"/>
        </svg>
        <span>www.website.com</span>
      </li>
      <li class="contact-item">
        <svg class="contact-icon" viewBox="0 0 26 26" fill="none" stroke="#fff" stroke-width="1.4">
          <circle cx="13" cy="13" r="12"/>
        </svg>
        <span>@yourname</span>
      </li>
    </ul>

    <p class="disclaimer">Paid for by the<br>Committe to Elect<br>Tall Ned Marsh<br>County Commissiner</p>
  </section>
</body>
</html>
```